Flyer-Design für feldwinkel.de
Zielgruppe
Wir vertreiben im Versandhandel über www.feldwinkel.de Pflanztöpfe/Schalen mit Selbstbewässerung. Der Hauptfokus liegt hier auf Grabschalen / Grabvasen
Aufgabenstellung
Flyer bitte im Format DIN-Lang.
Der Flyer soll sehr Bildhaft sein mit wenig Text.
Weitere Grafiken / Texte erhalten sie auch im Onlineshop www.feldwinkel.de

```html
<!DOCTYPE html>
<html lang="de">
<head>
<meta charset="utf-8">
<title>feldwinkel.de – Flyer DIN lang</title>
<link href="https://fonts.googleapis.com/css2?family=Open+Sans:wght@400;600;700&family=Kalam:wght@400;700&display=swap" rel="stylesheet">
<style>
  :root {
    --green: #a0b52b;
    --green-dark: #8a9d20;
    --pink: #f3a9c6;
    --cream: #f7f3e3;
    --ink: #2e2e2e;
    --white: #ffffff;
    --page: #ffffff;
  }
  * { box-sizing: border-box; margin: 0; padding: 0; }
  html, body { width: 1200px; height: 1200px; overflow: hidden; background: var(--page); }
  body { font-family: "Open Sans", Arial, sans-serif; color: var(--ink); position: relative; }

  .flyer {
    position: absolute; left: 80px; width: 1040px; height: 490px;
    box-shadow: 0 6px 22px rgba(0,0,0,.22); overflow: hidden; background: var(--white);
  }
  .flyer--front { top: 70px; }
  .flyer--back { top: 640px; }

  .photo { position: absolute; }
  .label-pink {
    position: absolute; background: var(--pink); color: var(--white);
    font-weight: 600; font-size: 25px; padding: 8px 20px; white-space: nowrap;
  }
  .brand { display: flex; align-items: center; gap: 10px; font-weight: 700; color: var(--green); }
  .brand-dot { width: 18px; height: 18px; border-radius: 50%; background: var(--pink); }

  /* Front side */
  .front-panel { position: absolute; left: 0; top: 0; width: 310px; height: 490px; background: var(--cream); }
  .front-panel .brand { position: absolute; left: 42px; top: 92px; font-size: 32px; }
  .front-band {
    position: absolute; left: 0; top: 190px; width: 310px; height: 210px;
    background: var(--green); color: var(--white); padding: 26px 22px;
  }
  .front-band .intro { font-family: "Kalam", cursive; font-size: 19px; line-height: 1.2; }
  .front-band .intro strong { font-size: 25px; font-weight: 700; }
  .benefits { list-style: none; margin-top: 14px; font-size: 14px; line-height: 1.75; }
  .benefits li { display: flex; align-items: center; gap: 8px; }
  .benefits svg { width: 16px; height: 16px; flex: none; }
  .contact { font-weight: 600; font-size: 15px; line-height: 1.45; text-align: center; }
  .front-panel .contact { position: absolute; left: 0; right: 0; top: 420px; }
  .front-photo {
    left: 310px; top: 0; width: 730px; height: 490px;
    background: linear-gradient(180deg, #a9c8e6 0%, #7c9a5a 35%, #6f8f46 55%, #9a9a98 80%, #b5b5b3 100%);
  }
  .front-photo + .label-pink { left: 330px; top: 300px; }

  /* Back side */
  .back-photo-main {
    left: 0; top: 0; width: 620px; height: 490px;
    background: linear-gradient(180deg, #f3eef3 0%, #f0e8ee 55%, #b79ad0 70%, #f5f3f5 100%);
  }
  .back-photo-main ~ .label-pink { left: 140px; top: 232px; font-size: 24px; }
  .flyer--back > .brand { position: absolute; left: 22px; top: 418px; font-size: 24px; }
  .back-photo-a { left: 620px; top: 0; width: 190px; height: 270px; background: linear-gradient(180deg, #5e7c6a, #9aa79a 60%, #c9c6bd); }
  .back-photo-b { left: 810px; top: 0; width: 230px; height: 140px; background: linear-gradient(180deg, #dfe3e6, #8b7b68); }
  .back-photo-c { left: 810px; top: 140px; width: 230px; height: 130px; background: linear-gradient(180deg, #b9cc7a, #e9ece4); }
  .back-panel {
    position: absolute; left: 620px; top: 270px; width: 420px; height: 220px;
    background: var(--green); color: var(--white); text-align: center; padding-top: 28px;
  }
  .back-panel .sizes { font-family: "Kalam", cursive; font-size: 17px; }
  .back-panel .shipping { font-family: "Kalam", cursive; font-weight: 700; font-size: 27px; line-height: 1.25; }
  .back-panel .invoice { font-family: "Kalam", cursive; font-size: 17px; }
  .back-panel .contact { margin-top: 22px; }
</style>
</head>
<body>

<section class="flyer flyer--front">
  <div class="front-panel">
    <div class="brand"><span class="brand-dot"></span>feldwinkel.de</div>
    <div class="front-band">
      <p class="intro">Ihr <strong>Onlineshop</strong> für Pflanzbehälter mit<br><strong>Selbstbewässerung...</strong></p>
      <ul class="benefits">
        <li><svg viewBox="0 0 16 16"><path d="M2 8l4 4 8-9" fill="none" stroke="#fff" stroke-width="2"/></svg>Edles und vielfältiges Design</li>
        <li><svg viewBox="0 0 16 16"><path d="M2 8l4 4 8-9" fill="none" stroke="#fff" stroke-width="2"/></svg>Vermeidung von Staunässe</li>
        <li><svg viewBox="0 0 16 16"><path d="M2 8l4 4 8-9" fill="none" stroke="#fff" stroke-width="2"/></svg>Wasserspeicher für bis zu 7 Tage</li>
      </ul>
    </div>
    <p class="contact">info@feldwinkel.de<br>www.feldwinkel.de</p>
  </div>
  <div class="photo front-photo" role="img" aria-label="Foto: silberne Grabschale mit Bepflanzung und Grabvase mit roten Rosen auf einem Grabstein im Friedhof"></div>
  <div class="label-pink">Grabschalen und Vasen</div>
</section>

<section class="flyer flyer--back">
  <div class="photo back-photo-main" role="img" aria-label="Foto: lila Blumenkasten mit roten Blüten neben einem pinken Windlicht"></div>
  <div class="photo back-photo-a" role="img" aria-label="Foto: Orchidee in Glasgefäß vor einer Vitrine"></div>
  <div class="photo back-photo-b" role="img" aria-label="Foto: weißes Pflanzgefäß auf einer Holzterrasse"></div>
  <div class="photo back-photo-c" role="img" aria-label="Foto: Kräutertöpfe in Grün und Grau auf einem Tisch"></div>
  <div class="label-pink">Blumenkästen, Kräutertöpfe und mehr...</div>
  <div class="brand"><span class="brand-dot"></span>feldwinkel.de</div>
  <div class="back-panel">
    <p class="sizes">Pflanzgefäße in verschiedenen Größen</p>
    <p class="shipping">Versandkostenfrei ab 99,00 €</p>
    <p class="invoice">Zahlung auf Rechnung möglich</p>
    <p class="contact">info@feldwinkel.de<br>www.feldwinkel.de</p>
  </div>
</section>

</body>
</html>
```